Alloy wheel repair business needs a website

Install logo previously purchased from pixelbazaar, toolbar with dropdowns. services, gallery, clients , contact ect
Maybe mission statment

Target Market(s)

vehicle owners, auto dealers,insurance companies,

Industry/Entity Type

Alloy Wheel Repair

Coding

Coded - Design and coding required

Number of Pages Required

4 page

Font styles to use
Sans Serif

Colors
0054AA
0677BA
7BADD7
CADEEF
E8F1F8

```html
<!DOCTYPE html>
<html lang="en">
<head>
<meta charset="utf-8">
<title>Rimcraft Works — Wheel Repair &amp; Service</title>
<link href="https://fonts.googleapis.com/css2?family=Montserrat:wght@300;400;500;600;700&display=swap" rel="stylesheet">
<style>
:root{
  --blue:#0054AA;
  --blue-mid:#0677BA;
  --blue-soft:#7BADD7;
  --blue-pale:#CADEEF;
  --panel:#E8ECF2;
  --line:#E2E5EA;
  --ink:#222426;
  --text:#3a3d40;
  --white:#fff;
}
*{box-sizing:border-box;margin:0;padding:0}
html,body{width:1200px;height:3025px;overflow:hidden;background:var(--white);font-family:'Montserrat',sans-serif;color:var(--text)}
.page{position:relative;width:1200px;height:3025px}
a{color:inherit;text-decoration:none}

/* header */
.site-header{position:absolute;left:0;top:0;width:1200px;height:105px;border-bottom:1px solid var(--line);box-shadow:0 2px 6px rgba(0,0,0,.04)}
.menu-btn{position:absolute;left:0;top:0;width:90px;height:105px;border-right:1px solid var(--line);display:flex;align-items:center;justify-content:center}
.search-btn{position:absolute;right:0;top:0;width:90px;height:105px;border-left:1px solid var(--line);display:flex;align-items:center;justify-content:center}
.brand{position:absolute;left:112px;top:36px;display:flex;align-items:center;gap:8px;font-weight:700;font-size:26px;color:var(--blue);letter-spacing:1px}
.brand-dot{width:14px;height:14px;border-radius:50%;background:var(--blue)}
.header-contact{position:absolute;right:325px;top:44px;display:flex;gap:28px;font-size:12px;font-weight:600;color:var(--ink)}
.header-contact span{display:flex;align-items:center;gap:6px}

/* hero */
.hero{position:absolute;left:90px;top:105px;width:1020px;height:479px;background:radial-gradient(ellipse at 35% 45%,#7c7a7a 0%,#3b3736 35%,#1c1a1a 65%),linear-gradient(90deg,#2a2626,#6b3a26);overflow:hidden}
.hero::after{content:"";position:absolute;inset:0;background:linear-gradient(100deg,rgba(0,0,0,0) 45%,rgba(150,70,35,.55) 80%,rgba(90,40,25,.7))}
.hero-copy{position:absolute;left:605px;top:168px;color:var(--white);z-index:2}
.hero-copy h1{font-size:36px;font-weight:700;line-height:1}
.hero-copy h1 .light{display:block;font-weight:300;font-size:44px;margin-top:2px}
.hero-copy p{font-size:10.5px;margin-top:12px}
.hero-btn{display:inline-block;margin-top:12px;border:1px solid var(--white);padding:6px 22px;font-size:11px}
.hero-arrow{position:absolute;top:230px;z-index:2}
.hero-dots{position:absolute;left:475px;top:452px;display:flex;gap:16px;align-items:center;z-index:2}
.hero-dots i{display:block;width:5px;height:5px;border-radius:50%;background:var(--white)}
.hero-dots i.on{width:10px;height:10px;background:none;border:1px solid var(--white)}

/* service tiles */
.services{position:absolute;left:90px;top:584px;width:1020px;height:246px;display:flex;border:1px solid var(--line);border-top:none}
.service{flex:1;border-right:1px solid var(--line);text-align:center;padding-top:65px;font-size:12.5px;color:var(--ink);line-height:1.3}
.service:last-child{border-right:none}
.service.active{background:var(--panel)}
.service svg.icon{display:block;margin:0 auto 22px}
.service .go{display:block;margin:12px auto 0}

/* about */
.about{position:absolute;left:0;top:880px;width:1200px;text-align:center}
.about h2{font-size:40px;font-weight:500;color:var(--ink);letter-spacing:.5px}
.about h3{font-size:17px;font-weight:500;color:var(--ink);line-height:1.4;margin-top:6px}
.about p{font-size:15px;line-height:1.6;width:750px;margin:20px auto 0}
.btn-blue{display:inline-flex;align-items:center;gap:8px;background:var(--blue-mid);color:var(--white);font-size:12px;padding:7px 22px}
.about .btn-blue{margin-top:24px}

/* feature grid */
.grid{position:absolute;left:89px;top:1168px;width:1022px;height:920px;display:grid;grid-template-columns:511px 511px;grid-template-rows:460px 460px;border:1px solid var(--line)}
.card{text-align:center;position:relative}
.card.tint{background:var(--panel)}
.card .shot{width:330px;height:180px;margin:48px auto 0;border-radius:6px}
.card .kicker{font-size:27px;font-weight:300;color:var(--ink);margin-top:40px;line-height:1.1}
.card .title{font-size:27px;font-weight:700;color:var(--ink);line-height:1.1}
.card p{font-size:15px;line-height:1.6;width:380px;margin:14px auto 0}
.card .go{display:block;margin:14px auto 0}
.shot-repair{background:linear-gradient(90deg,#d9d9d9 0%,#3a3a3a 30%,#8b8b8b 50%,#2b2b2b 75%,#1e1e1e 100%)}
.shot-color{background:linear-gradient(90deg,#222 0%,#1a1a1a 30%,#b33a2a 50%,#5a5a5a 70%,#c9c9c9 100%)}
.photo-oem{background:radial-gradient(ellipse at 40% 40%,#8d8d8d 0%,#3c3c3c 35%,#111 70%);position:relative}
.notch{position:absolute;right:0;top:200px;width:0;height:0;border-top:30px solid transparent;border-bottom:30px solid transparent;border-right:30px solid var(--white)}
.card.shop{padding-top:105px}
.card.shop p{width:400px}

/* coloring */
.coloring{position:absolute;left:0;top:2138px;width:1200px;text-align:center}
.coloring h2{font-size:28px;font-weight:600;color:var(--ink)}
.coloring p{font-size:15px;line-height:1.6;width:620px;margin:12px auto 0}
.gallery-band{position:absolute;left:89px;top:2290px;width:1022px;height:258px;background:var(--panel)}
.gallery-band::before{content:"";position:absolute;left:481px;top:0;border-left:30px solid transparent;border-right:30px solid transparent;border-top:30px solid var(--white)}
.wheels{position:absolute;left:56px;top:45px;width:630px;height:175px;border-radius:90px;background:linear-gradient(90deg,#a08060 0%,#2a2a2a 22%,#e0c020 42%,#6a2a8a 62%,#6b6050 82%,#c8c8c8 100%)}
.gallery-band .btn-blue{position:absolute;left:740px;top:120px;font-size:16px;padding:9px 28px;gap:14px}

/* locate */
.locate{position:absolute;left:89px;top:2548px;width:1022px;height:147px;border:1px solid var(--line);border-top:none;text-align:center;padding-top:55px}
.locate h2{font-size:28px;font-weight:600;color:var(--blue-mid)}
.locate p{font-size:17px;color:var(--ink);margin-top:6px}

/* footer */
.site-footer{position:absolute;left:89px;top:2695px;width:1022px;height:260px;background:var(--panel);font-size:11px;color:var(--ink)}
.f-col{position:absolute;top:50px}
.f-brand{left:35px}
.f-brand .brand{position:static;font-size:20px}
.f-brand h4{font-size:15px;font-weight:600;margin-top:16px}
.f-brand .addr{margin-top:6px;line-height:1.35;width:180px}
.f-brand .call{margin-top:16px}
.f-brand b{font-weight:600}
.f-col h5{font-size:15px;font-weight:600;margin-bottom:12px;margin-left:20px}
.f-col ul{list-style:none}
.f-col li{margin-bottom:9px;display:flex;gap:6px;align-items:center}
.f-links{left:309px;top:56px}
.f-support{left:585px;top:56px}
.f-social{left:781px;top:56px}
.f-social h5{margin-left:0}
.socials{display:flex;gap:8px}
.socials i{width:21px;height:21px;border-radius:50%;border:1px solid var(--ink);display:block}
.handle{font-size:13px;margin-top:8px}
.find{margin-top:30px;width:160px;border-bottom:1px solid var(--ink);display:flex;justify-content:space-between;color:#888;font-size:9px;padding-bottom:3px}
</style>
</head>
<body>
<div class="page">

  <header class="site-header">
    <div class="menu-btn">
      <svg width="24" height="16" viewBox="0 0 24 16"><path d="M0 1h24M0 8h24M0 15h24" stroke="#333" stroke-width="1.5"/></svg>
    </div>
    <a class="brand" href="#"><span class="brand-dot"></span>RIMCRAFT WORKS</a>
    <div class="header-contact">
      <span><svg width="12" height="16" viewBox="0 0 12 16"><path d="M6 1a5 5 0 0 1 5 5c0 4-5 9-5 9S1 10 1 6a5 5 0 0 1 5-5z" fill="none" stroke="#0677BA" stroke-width="1.5"/></svg>Find a Location</span>
      <span><svg width="12" height="14" viewBox="0 0 12 14"><path d="M3 1l2 3-1.5 1.5c.8 2 2 3.2 4 4L9 8l3 2-1.5 3C5 12 1 8 1 2z" fill="#0677BA"/></svg>555 014 2290</span>
    </div>
    <div class="search-btn">
      <svg width="26" height="26" viewBox="0 0 26 26"><circle cx="11" cy="11" r="9.5" fill="none" stroke="#333" stroke-width="1.6"/><path d="M18 18l6 6" stroke="#333" stroke-width="1.6"/></svg>
    </div>
  </header>

  <section class="hero" role="img" aria-label="Close-up photograph of a sports car alloy wheel at sunset">
    <svg class="hero-arrow" style="left:18px" width="10" height="18" viewBox="0 0 10 18"><path d="M9 1L1 9l8 8" fill="none" stroke="#fff" stroke-width="1.2"/></svg>
    <svg class="hero-arrow" style="right:18px" width="10" height="18" viewBox="0 0 10 18"><path d="M1 1l8 8-8 8" fill="none" stroke="#fff" stroke-width="1.2"/></svg>
    <div class="hero-copy">
      <h1>Nationwide Wheel<span class="light">Repair &amp; Service</span></h1>
      <p>High Quality Alloy Wheel Repair, OEM Replacements</p>
      <a class="hero-btn" href="#">Read More</a>
    </div>
    <div class="hero-dots"><i class="on"></i><i></i><i></i><i></i></div>
  </section>

  <nav class="services">
    <a class="service" href="#">
      <svg class="icon" width="60" height="60" viewBox="0 0 60 60"><circle cx="30" cy="30" r="28" fill="none" stroke="#222" stroke-width="3"/><circle cx="30" cy="30" r="19" fill="none" stroke="#222" stroke-width="2"/><circle cx="30" cy="30" r="5" fill="#222"/><path d="M30 11v14M30 35v14M11 30h14M35 30h14M17 17l9 9M34 34l9 9M43 17l-9 9M26 34l-9 9" stroke="#222" stroke-width="2"/></svg>
      WHEEL<br>REFINISHING
      <svg class="go" width="28" height="10" viewBox="0 0 28 10"><path d="M0 5h26M22 1l4 4-4 4" fill="none" stroke="#555" stroke-width="1.3"/></svg>
    </a>
    <a class="service active" href="#">
      <svg class="icon" width="64" height="60" viewBox="0 0 64 60"><circle cx="26" cy="30" r="24" fill="none" stroke="#222" stroke-width="6"/><circle cx="26" cy="30" r="6" fill="#222"/><path d="M26 12v12M26 36v12M8 30h12M32 30h12" stroke="#222" stroke-width="3"/><rect x="46" y="4" width="14" height="52" rx="4" fill="#222"/></svg>
      WHEEL<br>STRAIGHTENING
      <svg class="go" width="28" height="10" viewBox="0 0 28 10"><path d="M0 5h26M22 1l4 4-4 4" fill="none" stroke="#0677BA" stroke-width="1.5"/></svg>
    </a>
    <a class="service" href="#">
      <svg class="icon" width="56" height="60" viewBox="0 0 56 60"><circle cx="28" cy="24" r="22" fill="none" stroke="#222" stroke-width="3"/><circle cx="28" cy="24" r="10" fill="none" stroke="#222" stroke-width="3"/><circle cx="28" cy="24" r="4" fill="#222"/><rect x="4" y="46" width="48" height="10" rx="3" fill="none" stroke="#222" stroke-width="3"/></svg>
      WHEEL<br>REMANUFACTURING
      <svg class="go" width="28" height="10" viewBox="0 0 28 10"><path d="M0 5h26M22 1l4 4-4 4" fill="none" stroke="#555" stroke-width="1.3"/></svg>
    </a>
    <a class="service" href="#">
      <svg class="icon" width="60" height="60" viewBox="0 0 60 60"><circle cx="30" cy="30" r="28" fill="#222"/><circle cx="30" cy="30" r="19" fill="#8cc63f"/><circle cx="30" cy="30" r="6" fill="#fff"/><circle cx="30" cy="17" r="4" fill="#fff"/><circle cx="18" cy="36" r="4" fill="#fff"/><circle cx="42" cy="36" r="4" fill="#fff"/></svg>
      WHEEL<br>CUSTOM COLORING
      <svg class="go" width="28" height="10" viewBox="0 0 28 10"><path d="M0 5h26M22 1l4 4-4 4" fill="none" stroke="#555" stroke-width="1.3"/></svg>
    </a>
    <a class="service" href="#">
      <svg class="icon" width="72" height="60" viewBox="0 0 72 60"><circle cx="40" cy="28" r="26" fill="none" stroke="#222" stroke-width="3"/><circle cx="40" cy="28" r="16" fill="none" stroke="#222" stroke-width="2.5"/><path d="M40 12v32M24 28h32M29 17l22 22M51 17L29 39" stroke="#222" stroke-width="2.5"/><path d="M2 57h50" stroke="#222" stroke-width="3"/></svg>
      OEM WHEEL<br>SALES
      <svg class="go" width="28" height="10" viewBox="0 0 28 10"><path d="M0 5h26M22 1l4 4-4 4" fill="none" stroke="#555" stroke-width="1.3"/></svg>
    </a>
  </nav>

  <section class="about">
    <h2>ABOUT RIMCRAFT WORKS</h2>
    <h3>High Quality Alloy Wheel Repair,&nbsp; Custom Coloring &amp;<br>OEM Replacements</h3>
    <p>Lorem Ipsum is simply dummy text of the printing and typesetting industry. Lorem Ipsum has been the industry's standard dummy text ever since the 1500s, when an unknown printer took a galley of type and scrambled it to make a type specimen book.</p>
    <a class="btn-blue" href="#">Read More <svg width="18" height="8" viewBox="0 0 18 8"><path d="M0 4h16M13 1l3 3-3 3" fill="none" stroke="#fff" stroke-width="1.3"/></svg></a>
  </section>

  <section class="grid">
    <article class="card">
      <div class="shot shot-repair" role="img" aria-label="Product shot of a repair spray gun beside a red-accented alloy wheel and a tyre"></div>
      <div class="kicker">WHEEL</div>
      <div class="title">REPAIR SERVICES</div>
      <p>Lorem Ipsum is simply dummy text of the web and typesetting industry. e 1500s,</p>
      <svg class="go" width="30" height="10" viewBox="0 0 30 10"><path d="M0 5h28M24 1l4 4-4 4" fill="none" stroke="#555" stroke-width="1.3"/></svg>
    </article>
    <article class="card tint">
      <div class="shot shot-color" role="img" aria-label="Product shot of a tyre, a red-rimmed alloy wheel and a paint spray gun"></div>
      <div class="kicker">WHEEL</div>
      <div class="title">CUSTOM COLORING</div>
      <p>Lorem Ipsum is simply dummy text of the web and typesetting industry. e 1500s,</p>
      <svg class="go" width="30" height="10" viewBox="0 0 30 10"><path d="M0 5h28M24 1l4 4-4 4" fill="none" stroke="#555" stroke-width="1.3"/></svg>
    </article>
    <div class="card photo-oem" role="img" aria-label="Photograph of two chrome OEM alloy wheels on a dark background"><span class="notch"></span></div>
    <article class="card shop">
      <div class="kicker" style="margin-top:0">SHOP</div>
      <div class="title">OEM WHEELS</div>
      <p style="margin-top:28px">Lorem Ipsum is simply dummy text of the printing and typesetting industry. Lorem Ipsum has been the industry's standard dummy text<br>ever since the 1500s,</p>
      <p style="margin-top:24px">Shop OEM Wheels Lorem Ipsum has ever since 1968, Lorem Ipsum has been the industry's standard dummy text ever since the 1500s,</p>
      <svg class="go" width="30" height="10" viewBox="0 0 30 10"><path d="M0 5h28M24 1l4 4-4 4" fill="none" stroke="#555" stroke-width="1.3"/></svg>
    </article>
  </section>

  <section class="coloring">
    <h2>WHEEL CUSTOM COLORING</h2>
    <p>Lorem Ipsum is simply dummy text of the printing and typesetting industry. Lorem Ipsum has been the industry's standard dummy text ever since the 1500s,</p>
  </section>
  <div class="gallery-band">
    <div class="wheels" role="img" aria-label="Row of five custom-coloured alloy wheels in bronze, green, yellow, purple and gold"></div>
    <a class="btn-blue" href="#">See Our Gallery <svg width="22" height="10" viewBox="0 0 22 10"><path d="M0 5h20M16 1l4 4-4 4" fill="none" stroke="#fff" stroke-width="1.5"/></svg></a>
  </div>

  <section class="locate">
    <h2>FIND A WHEEL REPAIR LOCATION CLOSEST TO YOU</h2>
    <p>Then give us a Call or Request a Wheel Repair Request Online</p>
  </section>

  <footer class="site-footer">
    <div class="f-col f-brand">
      <span class="brand"><span class="brand-dot"></span>RIMCRAFT WORKS</span>
      <h4>Rimcraft Works</h4>
      <p class="addr">742 Orchard Lane, Brookfield PA 19990</p>
      <p class="call"><b>Call:</b> 555 014 2290</p>
      <p class="call" style="margin-top:14px"><b>Services:</b> 555 014 2290</p>
    </div>
    <div class="f-col f-links">
      <h5>Quick Links</h5>
      <ul>
        <li><svg width="14" height="6" viewBox="0 0 14 6"><path d="M0 3h12M10 1l2 2-2 2" fill="none" stroke="#555"/></svg>Wheel Repair Service</li>
        <li><svg width="14" height="6" viewBox="0 0 14 6"><path d="M0 3h12M10 1l2 2-2 2" fill="none" stroke="#555"/></svg>Wheel Custom Coloring</li>
        <li><svg width="14" height="6" viewBox="0 0 14 6"><path d="M0 3h12M10 1l2 2-2 2" fill="none" stroke="#555"/></svg>Shop OEM Wheels</li>
        <li><svg width="14" height="6" viewBox="0 0 14 6"><path d="M0 3h12M10 1l2 2-2 2" fill="none" stroke="#555"/></svg>Employee Access</li>
        <li><svg width="14" height="6" viewBox="0 0 14 6"><path d="M0 3h12M10 1l2 2-2 2" fill="none" stroke="#555"/></svg>Franchise Access</li>
        <li><svg width="14" height="6" viewBox="0 0 14 6"><path d="M0 3h12M10 1l2 2-2 2" fill="none" stroke="#555"/></svg>Tech Center</li>
      </ul>
    </div>
    <div class="f-col f-support">
      <h5>Support</h5>
      <ul>
        <li><svg width="14" height="6" viewBox="0 0 14 6"><path d="M0 3h12M10 1l2 2-2 2" fill="none" stroke="#555"/></svg>Customer Service</li>
        <li><svg width="14" height="6" viewBox="0 0 14 6"><path d="M0 3h12M10 1l2 2-2 2" fill="none" stroke="#555"/></svg>About Us</li>
        <li><svg width="14" height="6" viewBox="0 0 14 6"><path d="M0 3h12M10 1l2 2-2 2" fill="none" stroke="#555"/></svg>Contact us</li>
        <li><svg width="14" height="6" viewBox="0 0 14 6"><path d="M0 3h12M10 1l2 2-2 2" fill="none" stroke="#555"/></svg>Blog</li>
        <li><svg width="14" height="6" viewBox="0 0 14 6"><path d="M0 3h12M10 1l2 2-2 2" fill="none" stroke="#555"/></svg>Terms of Service</li>
      </ul>
    </div>
    <div class="f-col f-social">
      <h5>Stay Connected</h5>
      <div class="socials"><i></i><i></i><i></i><i></i><i></i><i></i></div>
      <p class="handle">@rimcraftworks</p>
      <div class="find"><span>Find location</span><svg width="10" height="10" viewBox="0 0 10 10"><circle cx="4" cy="4" r="3" fill="none" stroke="#333"/><path d="M6.5 6.5L9 9" stroke="#333"/></svg></div>
    </div>
  </footer>

</div>
</body>
</html>
```